Creation of a Velmaro Flyer design

As part of the cr% 26 # 233; ation of our soci% 26 # 233; t% 26 # 233 ;, we wish to cr% 26 # 233; er a flyer pr% 26 # 233; feeling our diff% 26 # 233; annuities% 26 # 233; s business advisory services% 26 # 233; foreign% 26 # 232; res who wish to develop their activities% 26 # 233; s in Switzerland. We want a double-sided flyer that presents% 26 # 233; society% 26 # 233; t% 26 # 233; d% 26 # 39; a c% 26 # 244; t% 26 # 233; and who presents% 26 # 233; benefits of the other. We have d% 26 # 233; j% 26 # 224; made a very basic provisional flyer to be able to present our activities. We put it to you as an example.

Target Market(s)

European companies% 26 # 233; internal% 26 # 233; res% 26 # 233; es by the market% 26 # 233; Swiss

Industry/Entity Type

Business Consultant

Colors

Designer to choose colors to be used in the design.

Requirements
Must have
• Company name and contact details
A field to detail the services
Nice to have
• Some% 26 # 233; l% 26 # 233; elements that recall Switzerland and some% 26 # 233; l% 26 # 233; elements that recall c% 26 # 244; t% 26 # 233; % 26quot; business% 26quot;

```html
<!DOCTYPE html>
<html lang="en">
<head>
<meta charset="utf-8">
<title>Velmaro Flyer</title>
<link href="https://fonts.googleapis.com/css2?family=Montserrat:wght@300;400;600&display=swap" rel="stylesheet">
<style>
  :root{
    --stage:#6b6c6e;
    --paper:#cfd7de;
    --ink:#262626;
    --white:#ffffff;
    --band-gray:#b5c0c9;
    --band-steel:#5e7f9b;
    --band-blue:#6b94b7;
    --band-bright:#7ba8cf;
    --band-mid:#6f92b1;
    --mark:#231f20;
  }
  html,body{margin:0;padding:0;width:1200px;height:1200px;overflow:hidden;background:var(--stage);}
  .flyer{
    position:absolute;left:170px;top:43px;
    width:904px;height:1170px;
    transform:scale(0.951);transform-origin:0 0;
    background:var(--paper);overflow:hidden;
    font-family:"Montserrat",sans-serif;color:var(--ink);
  }
  .flyer-shapes{position:absolute;inset:0;}
  .brand{position:absolute;left:48px;top:197px;display:flex;align-items:center;gap:28px;}
  .brand-square{width:56px;height:56px;border-radius:10px;background:var(--mark);}
  .brand-name{font-weight:300;font-size:46px;letter-spacing:2px;color:var(--mark);}
  .intro-panel{
    position:absolute;left:0;top:310px;width:685px;height:155px;
    background:rgba(255,255,255,0.42);
  }
  .intro-text{
    position:absolute;left:47px;top:322px;width:600px;margin:0;
    font-size:15.3px;line-height:25px;color:#2a2a2a;
  }
  .support-line{
    position:absolute;left:124px;top:506px;margin:0;
    font-size:15.5px;line-height:26px;color:var(--white);
  }
  .support-line strong{font-weight:600;font-size:26px;}
  .services{position:absolute;left:49px;top:785px;width:700px;}
  .services p{margin:0 0 26.5px;font-size:17px;line-height:26.5px;}
</style>
</head>
<body>
<div class="flyer">
  <svg class="flyer-shapes" viewBox="0 0 904 1170" width="904" height="1170">
    <defs>
      <linearGradient id="alpine" x1="0" y1="0" x2="0" y2="1">
        <stop offset="0" stop-color="#dfe4e9"/>
        <stop offset="0.45" stop-color="#c3ccd4"/>
        <stop offset="0.62" stop-color="#8e9aa0"/>
        <stop offset="0.78" stop-color="#4d5c40"/>
        <stop offset="1" stop-color="#2f3c28"/>
      </linearGradient>
    </defs>
    <rect class="alpine-photo" x="0" y="0" width="904" height="780" fill="url(#alpine)" role="img" aria-label="Photograph of a Swiss alpine valley with a pointed snowy peak, clouds and pine forest"/>
    <path class="band-gray" d="M0,0H904V325C780,205 400,175 0,85Z" fill="var(--band-gray)"/>
    <path class="band-steel" d="M0,0H904V290C760,165 380,145 0,50Z" fill="var(--band-steel)"/>
    <path class="band-blue" d="M160,0H904V165C700,110 400,150 160,0Z" fill="var(--band-blue)"/>
    <path class="band-left" d="M0,0H160C200,30 120,30 0,22Z" fill="var(--band-blue)"/>
    <path class="band-cloud" d="M255,0C330,50 500,42 640,0Z" fill="#a6b0b8"/>
    <path class="wave-light" d="M0,505C80,600 400,640 904,752V1170H0Z" fill="#c8d2da"/>
    <path class="wave-bright" d="M0,538C80,622 400,662 904,785V1170H0Z" fill="var(--band-bright)"/>
    <path class="wave-mid" d="M0,560C90,642 400,672 904,800V1170H0Z" fill="var(--band-mid)"/>
    <path class="paper-field" d="M0,670C150,760 500,742 780,800C880,850 860,1000 745,1170H0Z" fill="var(--paper)"/>
  </svg>

  <div class="brand">
    <div class="brand-square"></div>
    <div class="brand-name">VELMARO</div>
  </div>

  <div class="intro-panel"></div>
  <p class="intro-text">The potential of the Swiss market offers many business opportunities to foreign companies, however there are some tariff and non-tariff barriers to cope with, such as its strong requirements in terms of quality and innovation, cultural and linguistic differences, specific rules applied to certain products or services.</p>

  <p class="support-line"><strong>Velmaro</strong> is there to support you<br>in your administrative and strategic procedures!</p>

  <div class="services">
    <p>Velmaro strives to deepen the understanding of your business and acts as your local partner. We assist you in defining together all the services that best meet your needs.</p>
    <p>Our consulting skills are focused on high added value sectors, such as food and beverages, fashion &amp; lifestyle, products and services for leading industries (pharmaceutical, chemical, precision mechanics) or sustainable solutions (renewable energies, recyclable materials).</p>
    <p>From our office in Neuchâtel* and with our language knowledges, we are able to cover the whole of Switzerland. Having many years of experience in economic promotion and business management, we are familiar with the Swiss trade and foreign companies wishing to export to Switzerland.</p>
  </div>
</div>
</body>
</html>
```